Coming Soon page for a new fitness startup

We are a new startup based in Toronto, Canada working on a site and mobile app where people can register for athletic events such as running, cycling, triathlon, SUP, etc.

Participants will also be able to manage their clubs and team, and connect their fitness trackers so they have all their fitness data and friends in one place.

I like very simple designs and lots of whitespace. So no need for icons or unnecessary graphics.

I prefer having a mobile phone app instead of a hero image. No need to worry about the details within the mobile app for now, we can fill it in later. Here are some landing pages that I like.
https://pixelvault.example/torvanmelk/buckets/438197-Landing-Page

Attached is a wireframe that gives some sample content for each of the sections. Please do not take the wireframe too literally, it is only meant to illustrate the content that we are experimenting with and should give an idea of how much text will be on the page.

I have also attached the company logo files. The logo is not being used yet so feel free to simplify the logo if it doesn't look great with your design. For example, I'm ok with just the name "k7ravi" in white if that looks better.

Target Market(s)

Ages 25 to 45. Interested in running, cycling, triathlon, SUP, etc.

Industry/Entity Type

Fitness

Coding

Coded - Design and coding required

Number of Pages Required

1 page

Requirements
Should not have
• Any photos should not contain track and field events, or people in a gym. Any photos should have people running or cycling outdoors. I know that photos can be easily swapped out but it is distracting to review a design that has the wrong photos.

```html
<!DOCTYPE html>
<html lang="en">
<head>
<meta charset="utf-8">
<title>k7ravi — Launching Spring 2018</title>
<link rel="stylesheet" href="https://fonts.googleapis.com/css2?family=Catamaran:wght@500;600;700&family=Roboto:wght@300;400;500&display=swap">
<style>
  :root {
    --red: #d2202f;
    --ink: #555557;
    --text: #5c5c5e;
    --hero-bg: #efefef;
    --panel: #58585a;
    --footer: #3a3a3c;
    --white: #ffffff;
  }
  * { box-sizing: border-box; margin: 0; padding: 0; }
  html, body { width: 887px; height: 1200px; overflow: hidden; }
  body { position: relative; font-family: "Roboto", sans-serif; color: var(--text); background: var(--white); }

  .hero { position: absolute; left: 0; top: 0; width: 887px; height: 494px;
    background: linear-gradient(135deg, #f3f3f3 0%, #ebebeb 55%, #f1f1f1 100%); }
  .brand { position: absolute; left: 63px; top: 14px; display: flex; align-items: center; gap: 8px; }
  .brand-dot { width: 28px; height: 28px; border-radius: 50%; border: 3px solid var(--red); }
  .brand-name { font-family: "Catamaran", sans-serif; font-weight: 600; font-size: 26px; color: var(--ink); line-height: 1; }
  .launch { position: absolute; right: 63px; top: 22px; font-family: "Catamaran", sans-serif; font-weight: 600; font-size: 17px; color: var(--red); }

  .app-preview { position: absolute; left: 22px; top: 84px; width: 314px; height: 410px;
    background: radial-gradient(ellipse at 55% 45%, #ffffff 0%, #f2dfe1 35%, #e9c9b8 70%, #ececec 100%);
    border-radius: 20px 20px 0 0; }

  .hero-copy { position: absolute; left: 359px; top: 142px; width: 470px; }
  .hero-title { font-family: "Catamaran", sans-serif; font-weight: 600; font-size: 32px; line-height: 37px; color: var(--ink); }
  .hero-lead { margin-top: 10px; font-size: 16px; line-height: 20px; color: var(--text); font-weight: 400; }
  .hero-invite { margin-top: 22px; font-size: 15.5px; line-height: 19px; color: var(--red); font-weight: 400; }
  .notify { position: absolute; left: 359px; top: 373px; display: flex; gap: 9px; }
  .field { background: var(--white); border: 1px solid #dedede; font-family: "Roboto", sans-serif; font-size: 10px; color: #555; padding: 0 10px; display: flex; align-items: center; }
  .notify .field { width: 322px; height: 39px; }
  .btn { background: var(--red); color: var(--white); font-family: "Roboto", sans-serif; font-weight: 500; font-size: 12.5px; display: flex; align-items: center; justify-content: center; }
  .notify .btn { width: 122px; height: 40px; }

  .features { position: absolute; left: 0; top: 494px; width: 887px; height: 300px; }
  .features-title { position: absolute; top: 55px; width: 100%; text-align: center; font-family: "Catamaran", sans-serif; font-weight: 700; font-size: 33px; color: var(--red); }
  .features-sub { position: absolute; top: 98px; width: 100%; text-align: center; font-size: 17px; font-weight: 300; color: var(--text); }
  .feature { position: absolute; top: 150px; width: 220px; }
  .feature h3 { font-family: "Catamaran", sans-serif; font-weight: 500; font-size: 15.5px; color: var(--ink); }
  .feature p { margin-top: 8px; font-size: 11.5px; line-height: 15.3px; font-weight: 300; color: var(--text); }

  .organizers { position: absolute; left: 0; top: 794px; width: 887px; height: 363px; background: var(--red); color: var(--white); }
  .org-copy { position: absolute; left: 63px; top: 70px; width: 335px; }
  .org-copy h2 { font-family: "Catamaran", sans-serif; font-weight: 600; font-size: 27px; line-height: 30px; }
  .org-copy h4 { font-family: "Catamaran", sans-serif; font-weight: 500; font-size: 19px; margin-top: 2px; }
  .org-copy p { margin-top: 12px; font-size: 12.8px; line-height: 17px; font-weight: 400; }
  .org-copy .learn { display: block; margin-top: 18px; font-family: "Catamaran", sans-serif; font-weight: 600; font-size: 12.5px; }

  .contact { position: absolute; left: 425px; top: 40px; width: 398px; height: 293px; background: var(--panel); padding: 14px 15px; }
  .contact h2 { font-family: "Catamaran", sans-serif; font-weight: 600; font-size: 26px; line-height: 30px; }
  .contact .field { width: 364px; height: 43px; margin-top: 13px; border: none; border-radius: 2px; font-size: 11px; color: #777; }
  .contact .field:first-of-type { margin-top: 14px; }
  .contact .btn { position: absolute; right: 21px; bottom: 12px; width: 121px; height: 39px; }

  .site-footer { position: absolute; left: 0; top: 1157px; width: 887px; height: 43px; background: var(--footer); color: var(--white); font-size: 10px; }
  .footer-links { position: absolute; left: 63px; top: 15px; }
  .social { position: absolute; left: 412px; top: 14px; display: flex; gap: 13px; }
  .social span { width: 13px; height: 13px; border-radius: 50%; background: var(--white); display: block; }
  .copyright { position: absolute; right: 63px; top: 15px; }
</style>
</head>
<body>
  <header class="hero">
    <div class="brand"><span class="brand-dot"></span><span class="brand-name">k7ravi</span></div>
    <div class="launch">Launching Spring 2018</div>
    <div class="app-preview" role="img" aria-label="Photo of a hand holding a smartphone showing the app home screen"></div>
    <div class="hero-copy">
      <h1 class="hero-title">Connect Your Training, Friends, and Events in One Place</h1>
      <p class="hero-lead">Lorem ipsum dolor sit amet, consectetuer adipiscing elit, sed diam nonummy nibh euismod tincidunt ut laoreet dolore magna aliquam erat volutpat.</p>
      <p class="hero-invite">Join our email list. A referral program is coming and you'll want to be the first to know.</p>
    </div>
    <div class="notify">
      <div class="field">Enter Email Address</div>
      <div class="btn">Notify Me</div>
    </div>
  </header>

  <section class="features">
    <h2 class="features-title">Training and Racing all in one place</h2>
    <p class="features-sub">A new fitness community is coming soon.</p>
    <div class="feature" style="left:63px">
      <h3>Find Events</h3>
      <p>Lorem ipsum dolor sit amet, consectetuer adipiscing elit, sed diam nonummy nibh euismod tincidunt ut laoreet dolore magna aliquam erat volutpat.</p>
    </div>
    <div class="feature" style="left:347px">
      <h3>Invite Your Friends</h3>
      <p>Lorem ipsum dolor sit amet, consectetuer adipiscing elit, sed diam nonummy nibh euismod tincidunt ut laoreet dolore magna aliquam erat volutpat.</p>
    </div>
    <div class="feature" style="left:615px">
      <h3>Connect Your Workouts</h3>
      <p>Lorem ipsum dolor sit amet, consectetuer adipiscing elit, sed diam nonummy nibh euismod tincidunt ut laoreet dolore magna aliquam erat volutpat.</p>
    </div>
  </section>

  <section class="organizers">
    <div class="org-copy">
      <h2>Organizing an event?</h2>
      <h4>Attracting participants is hard</h4>
      <p>with your event listed on k7ravi we'll not only handle the registration and payment process, we've also made it our own personal mission to drive up participation numbers across all events.</p>
      <span class="learn">Contact us to learn more</span>
    </div>
    <div class="contact">
      <h2>We'd love to hear from you</h2>
      <div class="field">Your Name</div>
      <div class="field">Email Address</div>
      <div class="field">How can we help?</div>
      <div class="btn">Send Now</div>
    </div>
  </section>

  <footer class="site-footer">
    <div class="footer-links">About Us &nbsp;|&nbsp; Developers &nbsp;|&nbsp; Careers</div>
    <div class="social"><span aria-label="Social link"></span><span aria-label="Social link"></span><span aria-label="Social link"></span></div>
    <div class="copyright">© 2018 K7ravi Inc.</div>
  </footer>
</body>
</html>
```